Tonic und Gin Tonic
Zielgruppe
Von Altenburg in alle Welt
Heute arbeiten über 65 Mitarbeiter aus der Region. Auf 30.000 Quadratmetern werden täglich 200.000 Flaschen Hochprozentiges produziert und abgefüllt. Weitere Produktionsflächen auf 85.000 Quadratmetern in Polen dienen ebenfalls der Unternehmensaktivität Mit einer Produktion von mehr als 30 Millionen Flaschen im Jahr ist die Brennhofer Destillerie heute einer der größten Spirituosenhersteller Deutschlands. Und in der Tat könnte man sich hier verlaufen. Die Lagerkapazität reicht für zwei Millionen Flaschen. Die Getränkeauswahl ist immens. Die Produktion erfolgt auf acht automatisierten Abfülllinien. Die Brennhofer Spezialitäten werden ins In- und Ausland verschickt. Nach Israel, nach China und Amerika – die Liste ist lang. „Wir haben mehr als 120 verschiedene Produkte im Programm, Frucht- und Sahneliköre, Klare und Kräuterschnäpse“.
Neben Glas und PET fertigen wir Dosen in 200 ml, 250 ml slim, 330 ml und 500 ml.
Aufgabenstellung
Kreativ, einzigartig, ansprechend, marktkonform und realistisch, keine Kunst! Da wir bereits mit nationalen und internationalen Firmen zusammenarbeiten, auch Polen, Bulgarien und Rumänien kennen wir die Preislage bezüglich Design und Entwicklung und suchen einen Partner / Designer, mehr Leistung erbringen kann als versprochen wird.
Bei Interesse streben wir eine langfristige Zusammenarbeit an.
Im Anhang finden Sie Bildmaterial, was von einem anderen Produkt stammt mit Copyright!. Es geht be der Entwicklung um eine Dose von 250 ml Slim.
Es geht um die Entwicklung eines Design für ein neues Dosengetränk. Weitere Feinheiten und Einzelheiten per Telefon und oder Email.

```html
<!DOCTYPE html>
<html lang="de">
<head>
<meta charset="utf-8">
<title>Brennhofer Tonic – Dosendesign 250 ml slim</title>
<link rel="stylesheet" href="https://fonts.googleapis.com/css2?family=Cormorant+SC:wght@600&family=Cormorant+Garamond:wght@500&display=swap">
<style>
  :root {
    --stage: #efece6;
    --teal: #12a39c;
    --teal-deep: #0c7f79;
    --ink: #1b1a1a;
    --can-black: #0b0b0b;
    --rim: #c9ccce;
    --paper: #ffffff;
  }
  * { box-sizing: border-box; margin: 0; padding: 0; }
  html, body { width: 1200px; height: 688px; overflow: hidden; }
  body {
    background: var(--stage);
    position: relative;
    font-family: "Cormorant Garamond", serif;
  }

  /* square label artwork */
  .label {
    position: absolute;
    left: 200px; top: 124px;
    width: 440px; height: 440px;
    background: var(--teal);
    border: 5px solid var(--paper);
    box-shadow: 0 2px 10px rgba(0,0,0,.12);
  }
  .brand {
    position: absolute;
    left: 0; right: 0; top: 118px;
    text-align: center;
    font-family: "Cormorant SC", serif;
    font-weight: 600;
    color: var(--ink);
    line-height: 1;
  }
  .brand-name { display: block; font-size: 44px; letter-spacing: 2px; }
  .brand-product { display: block; font-size: 104px; letter-spacing: 4px; margin-top: 4px; }
  .tagline {
    position: absolute;
    left: 0; right: 0; bottom: 10px;
    text-align: center;
    font-variant: small-caps;
    font-size: 20px;
    letter-spacing: 1.5px;
    color: var(--paper);
  }

  /* flat can front */
  .can {
    position: absolute;
    left: 780px; top: 40px;
    width: 230px; height: 608px;
    background: var(--can-black);
    border-top: 8px solid var(--rim);
    border-bottom: 8px solid var(--rim);
    border-radius: 10px;
    overflow: hidden;
  }
  .can-band {
    position: absolute;
    left: 0; right: 0; top: 150px; height: 290px;
    background: linear-gradient(90deg, var(--teal-deep), var(--teal) 45%, var(--teal-deep));
    border-top: 2px solid var(--paper);
    border-bottom: 2px solid var(--paper);
  }
  .can-band .brand { top: 74px; }
  .can-band .brand-name { font-size: 24px; letter-spacing: 1px; }
  .can-band .brand-product { font-size: 54px; letter-spacing: 2px; margin-top: 2px; }
  .can-band .tagline { font-size: 12px; letter-spacing: 1px; bottom: 8px; }
  .volume {
    position: absolute;
    left: 8px; bottom: 10px;
    font-family: "Cormorant Garamond", serif;
    font-size: 10px;
    color: var(--paper);
  }
</style>
</head>
<body>

  <section class="label">
    <div class="brand">
      <span class="brand-name">Brennhofer</span>
      <span class="brand-product">Tonic</span>
    </div>
    <p class="tagline">A superior Tonic Water</p>
  </section>

  <section class="can">
    <div class="can-band">
      <div class="brand">
        <span class="brand-name">Brennhofer</span>
        <span class="brand-product">Tonic</span>
      </div>
      <p class="tagline">A superior Tonic Water</p>
    </div>
    <span class="volume">250 ml</span>
  </section>

</body>
</html>
```